Rig up a website for a Rigging Company

We already have a logo. Looking for a website design that works on plivano.com.
Our rigging company uses semi trucks, forklifts, and similar equipment to move large machines.
Our logo is white, black and red.

Target Market(s)

Medical Industry (moving medical equipment), Utility Industry (power equipment), Food Industry (moving bottling/packing equipment), US Government (large equipment)

Industry/Entity Type

It Company

Coding

Coded - Design and coding required

Number of Pages Required

5+ page

Font styles to use
Sans Serif

Colors
ec1f27
ffffff
0355a3

Requirements
Must have
• Home page, About page, Services Page, and Contact Information page
Nice to have
• Pictures of semi and forklifts and ability to insert our own pictures of our equipment

```html
<!DOCTYPE html>
<html lang="en">
<head>
<meta charset="utf-8">
<title>Halden Rigging</title>
<link rel="stylesheet" href="https://fonts.googleapis.com/css2?family=Open+Sans:ital,wght@0,400;0,600;0,700;0,800;1,700;1,800&display=swap">
<style>
:root{
  --red:#ec1f27;
  --red-dark:#c8151c;
  --ink:#1d1d1d;
  --text:#555;
  --muted:#8a8a8a;
  --line:#e2e2e2;
  --bar:#111;
  --white:#fff;
  --blue:#0355a3;
}
*{box-sizing:border-box;margin:0;padding:0}
html,body{width:1200px;height:3520px;overflow:hidden}
body{font-family:"Open Sans",Arial,sans-serif;color:var(--text);background:var(--white);position:relative}
.abs{position:absolute}

/* top bar */
.topbar{left:0;top:0;width:1200px;height:32px;background:var(--bar);color:#ddd;font-size:12px;display:flex;align-items:center;padding:0 72px}
.topbar .item{display:flex;align-items:center;gap:6px;margin-right:180px}
.topbar .item:nth-child(2){margin-left:120px;margin-right:auto}
.topbar .socials{display:flex;gap:5px}
.dot{width:16px;height:16px;border-radius:50%;display:inline-block}

/* nav */
.nav{left:0;top:32px;width:1200px;height:56px;background:var(--white);display:flex;align-items:center;justify-content:space-between;padding:0 72px 0 80px}
.brand{font-weight:800;font-size:26px;color:var(--ink);display:flex;align-items:center;gap:8px}
.brand .sq{width:14px;height:14px;background:var(--red)}
.menu{display:flex;height:56px}
.menu a{display:flex;align-items:center;padding:0 22px;font-size:14px;font-weight:700;color:var(--ink);text-decoration:none}
.menu a.active{background:var(--red);color:var(--white)}

/* hero */
.hero{left:0;top:88px;width:1200px;height:652px;background:linear-gradient(180deg,#5a5a58 0%,#3c3c3b 45%,#232323 100%)}
.hero-copy{left:0;top:430px;width:1200px;text-align:center;color:var(--white)}
.hero-copy h1{font-size:40px;font-style:italic;font-weight:800}
.hero-copy p{font-size:17px;font-style:italic;margin-top:4px;line-height:1.3}
.btn{display:inline-block;background:var(--red);color:var(--white);font-size:12px;font-weight:700;padding:9px 22px;letter-spacing:.5px}
.hero-copy .btn{margin-top:20px}

/* band */
.band{left:0;top:740px;width:1200px;height:120px;background:linear-gradient(90deg,var(--red-dark),var(--red) 50%,var(--red-dark));display:flex;align-items:center;justify-content:center;gap:110px}
.band h2{color:var(--white);font-style:italic;font-weight:800;font-size:21px;letter-spacing:1px}
.band .quote{background:var(--white);color:var(--ink);font-size:13px;font-weight:800;padding:10px 20px}

/* section headings */
.heading{left:0;width:1200px;text-align:center}
.heading h2{font-size:26px;font-weight:800;color:var(--ink);letter-spacing:1px}
.heading .sub{font-size:14px;color:var(--text);margin-top:4px}
.orn{display:flex;align-items:center;justify-content:center;gap:12px;margin-top:10px}
.orn span{width:90px;height:2px;background:var(--ink)}

/* about */
.about-text{left:72px;top:1000px;width:1056px;font-size:13px;line-height:1.6;color:var(--text)}
.about-btn{left:0;top:1160px;width:1200px;text-align:center}
.rule{left:72px;width:1056px;height:1px;background:var(--line)}

/* services */
.cats{left:0;top:1380px;width:1200px;text-align:center;font-size:14px;font-weight:600;color:var(--ink);word-spacing:2px}
.cats span{margin:0 18px}
.filters{left:0;top:1440px;width:1200px;text-align:center;font-size:13px;font-weight:700;color:var(--ink)}
.filters span{margin:0 10px}
.filters .on{color:var(--red)}
.tile{background:linear-gradient(160deg,#9aa1a8,#5d636a)}
.logo-tile{background:var(--white);border:1px solid var(--line);display:flex;align-items:center;justify-content:center}

/* testimonials */
.cards{left:72px;top:2440px;width:1056px;display:flex;justify-content:space-between}
.card{width:330px;text-align:center}
.avatar{width:84px;height:84px;border-radius:50%;margin:0 auto;background:linear-gradient(160deg,#d9c3a8,#8b6f58);border:3px solid #eee}
.card h4{font-size:14px;color:var(--ink);margin-top:14px;font-weight:700}
.card .role{font-size:12px;color:var(--muted)}
.card .box{margin-top:16px;border:1px solid var(--line);padding:26px 24px;font-size:13px;line-height:1.6;min-height:150px;box-shadow:0 2px 6px rgba(0,0,0,.06)}
.pager{left:0;top:2760px;width:1200px;display:flex;justify-content:center;gap:10px}
.pager i{width:12px;height:12px;border-radius:50%;background:#ccc}
.pager i.on{background:var(--red)}

/* newsletter */
.news{left:0;top:2840px;width:1200px;height:220px;background:linear-gradient(180deg,#262626,#141414);text-align:center;color:var(--white);padding-top:38px}
.news h2{font-size:26px;font-weight:800}
.news p{font-size:13px;letter-spacing:1px;margin-top:4px}
.form{display:flex;justify-content:center;margin-top:24px}
.form .field{width:420px;height:36px;background:var(--white);color:var(--muted);font-size:12px;text-align:left;padding:10px 14px}
.form .submit{width:100px;height:36px;background:var(--red);font-size:12px;font-weight:700;padding-top:10px}

/* contact */
.contacts{left:72px;top:3200px;width:1056px;display:flex;justify-content:space-around}
.contact{width:300px;text-align:center}
.ci{width:76px;height:76px;border-radius:50%;margin:0 auto;display:flex;align-items:center;justify-content:center;background:var(--ink)}
.ci.red{background:var(--red)}
.contact h4{font-size:15px;color:var(--ink);margin-top:14px;font-weight:800}
.contact p{font-size:13px;line-height:1.5}
.csocial{left:0;top:3415px;width:1200px;display:flex;justify-content:center;gap:8px}
.csocial .dot{width:22px;height:22px}

.footer{left:0;top:3466px;width:1200px;height:54px;background:var(--red);color:var(--white);font-size:12px;font-weight:700;display:flex;align-items:center;padding:0 72px}
</style>
</head>
<body>

<div class="abs topbar">
  <div class="item">
    <svg width="14" height="10" viewBox="0 0 14 10"><rect x=".5" y=".5" width="13" height="9" fill="none" stroke="#ddd"/><path d="M1 1l6 5 6-5" fill="none" stroke="#ddd"/></svg>
    info@haldenrigging.com
  </div>
  <div class="item">
    <svg width="12" height="12" viewBox="0 0 24 24"><path fill="#ddd" d="M6.6 10.8a15 15 0 006.6 6.6l2.2-2.2a1 1 0 011-.25 11 11 0 003.6.6 1 1 0 011 1V20a1 1 0 01-1 1A17 17 0 013 4a1 1 0 011-1h3.5a1 1 0 011 1 11 11 0 00.6 3.6 1 1 0 01-.25 1z"/></svg>
    555 814 2290
  </div>
  <div class="socials">
    <span class="dot" style="background:#3b5998"></span>
    <span class="dot" style="background:#1da1f2"></span>
    <span class="dot" style="background:#dd4b39"></span>
    <span class="dot" style="background:#cb2027"></span>
    <span class="dot" style="background:#f26522"></span>
  </div>
</div>

<header class="abs nav">
  <div class="brand"><span class="sq"></span>Halden Rigging</div>
  <nav class="menu">
    <a class="active">HOME</a><a>ABOUT</a><a>SERVICES</a><a>CONTACT</a><a>BLOG</a>
  </nav>
</header>

<div class="abs hero" role="img" aria-label="Two yellow forklifts parked in a dark warehouse"></div>
<div class="abs hero-copy">
  <h1>Welcome To Halden Rigging</h1>
  <p>Lorem Ipsum is simply dummy text of the printing<br>and type setting industry.</p>
  <span class="btn">READ MORE</span>
</div>

<section class="abs band">
  <h2>PROVIDING OUR CUSTOMER WITH THE BEST SOLUTION</h2>
  <span class="quote">GET A QUOTE</span>
</section>

<div class="abs heading" style="top:912px">
  <h2>ABOUT</h2>
  <div class="orn"><span></span><svg width="22" height="22" viewBox="0 0 22 22"><path d="M11 1l10 10-10 10L1 11z" fill="#1d1d1d"/></svg><span></span></div>
</div>
<p class="abs about-text">Lorem Ipsum is simply dummy text of the printing and typesetting industry. Lorem Ipsum has been the industry's standard dummy text ever since the 1500s, when an unknown printer took a galley of type and scrambled it to make a type specimen book. It has survived not only five centuries, but also the leap into electronic typesetting, remaining essentially unchanged. It was popularised in the 1960s with the release of Letraset sheets containing Lorem Ipsum passages, and more recently with desktop publishing software like Aldus PageMaker including versions of Lorem Ipsum.</p>
<div class="abs about-btn"><span class="btn">READ MORE</span></div>

<div class="abs rule" style="top:1262px"></div>

<div class="abs heading" style="top:1310px">
  <h2>WE MAKE THE BEST SERVICES</h2>
</div>
<div class="abs cats"><span>SEMI TRUCKS</span><span>FORKLIFTS</span><span>SIMILAR EQUIPMENT</span><span>LARGE MACHINES</span></div>
<div class="abs filters"><span class="on">All</span><span>Video Forklift</span><span>Video Truck</span><span>Services Truck</span><span>Services Forklift</span></div>

<div class="abs tile" style="left:72px;top:1512px;width:268px;height:208px;background:linear-gradient(160deg,#cfd8e0,#7d8894)" role="img" aria-label="White semi truck on the road"></div>
<div class="abs tile" style="left:344px;top:1512px;width:256px;height:208px;background:linear-gradient(160deg,#8a7a55,#4a4538)" role="img" aria-label="Row of yellow forklifts in a warehouse"></div>
<div class="abs tile" style="left:604px;top:1512px;width:524px;height:428px;background:linear-gradient(160deg,#9ea3a6,#4c5053)" role="img" aria-label="Red forklift lifting a large stone block"></div>
<div class="abs tile" style="left:72px;top:1724px;width:528px;height:216px;background:linear-gradient(160deg,#b8c0c8,#59626b)" role="img" aria-label="Forklift outside an industrial building"></div>
<div class="abs tile" style="left:72px;top:1948px;width:260px;height:212px;background:linear-gradient(160deg,#a6a27a,#5d5a40)" role="img" aria-label="Yellow telehandler on site"></div>
<div class="abs tile" style="left:336px;top:1948px;width:260px;height:212px;background:linear-gradient(160deg,#e6e6e6,#9a9a8a)" role="img" aria-label="Yellow forklift on white background"></div>
<div class="abs logo-tile" style="left:600px;top:1948px;width:260px;height:212px"><div class="brand"><span class="sq"></span>Halden Rigging</div></div>
<div class="abs tile" style="left:864px;top:1948px;width:264px;height:212px;background:linear-gradient(160deg,#6f6f6c,#2e2e2c)" role="img" aria-label="Forklift in a dim warehouse"></div>

<div class="abs rule" style="top:2236px"></div>

<div class="abs heading" style="top:2290px">
  <h2>WHAT CLIENTS SAY ABOUT US</h2>
  <div class="sub">Our Testimonials</div>
  <div class="orn"><span></span><svg width="22" height="22" viewBox="0 0 22 22"><path d="M11 1l10 10-10 10L1 11z" fill="#1d1d1d"/></svg><span></span></div>
</div>

<div class="abs cards">
  <div class="card">
    <div class="avatar" role="img" aria-label="Client portrait"></div>
    <h4>Jane Doe</h4><div class="role">Engineer of Media Production</div>
    <div class="box">Lorem ipsum dolor sit amet, consectetur adipiscing elit. Morbi vestibulum nulla imperdiet fermentum molestie, sed vitae.</div>
  </div>
  <div class="card">
    <div class="avatar" role="img" aria-label="Client portrait"></div>
    <h4>Jane Doe</h4><div class="role">Engineer of Media Production</div>
    <div class="box">Lorem ipsum dolor sit amet, consectetur adipiscing elit. Morbi vestibulum nulla imperdiet fermentum molestie, sed vitae.</div>
  </div>
  <div class="card">
    <div class="avatar" role="img" aria-label="Client portrait"></div>
    <h4>John Doe</h4><div class="role">Engineer of Media Production</div>
    <div class="box">Lorem ipsum dolor sit amet, consectetur adipiscing elit. Morbi vestibulum nulla imperdiet fermentum molestie, sed vitae.</div>
  </div>
</div>
<div class="abs pager"><i></i><i></i><i class="on"></i></div>

<section class="abs news">
  <h2>SUBSCRIBE TO OUR NEWSLETTER</h2>
  <p>TO RECEIVE THE LATEST NEWS &amp; UPDATE</p>
  <div class="form"><div class="field">Your Email</div><div class="submit">SUBMIT</div></div>
</section>

<div class="abs heading" style="top:3090px">
  <h2>CONTACT US</h2>
  <div class="orn"><span></span><svg width="22" height="22" viewBox="0 0 22 22"><path d="M11 1l10 10-10 10L1 11z" fill="#1d1d1d"/></svg><span></span></div>
</div>

<div class="abs contacts">
  <div class="contact">
    <div class="ci red"><svg width="30" height="36" viewBox="0 0 24 30"><path fill="#fff" d="M12 0a10 10 0 00-10 10c0 8 10 20 10 20s10-12 10-20A10 10 0 0012 0zm0 14a4 4 0 110-8 4 4 0 010 8z"/></svg></div>
    <h4>ADDRESS</h4>
    <p>2280 Harbor Mill Road,<br>Suite 410</p>
  </div>
  <div class="contact">
    <div class="ci"><svg width="34" height="24" viewBox="0 0 34 24"><rect x="1" y="1" width="32" height="22" fill="#fff"/><path d="M1 1l16 12L33 1" fill="none" stroke="#1d1d1d" stroke-width="2"/></svg></div>
    <h4>PHONE</h4>
    <p>office@haldenrigging.com</p>
  </div>
  <div class="contact">
    <div class="ci"><svg width="32" height="32" viewBox="0 0 24 24"><path fill="#fff" d="M6.6 10.8a15 15 0 006.6 6.6l2.2-2.2a1 1 0 011-.25 11 11 0 003.6.6 1 1 0 011 1V20a1 1 0 01-1 1A17 17 0 013 4a1 1 0 011-1h3.5a1 1 0 011 1 11 11 0 00.6 3.6 1 1 0 01-.25 1z"/></svg></div>
    <h4>EMAIL</h4>
    <p>+1 (0) 555 000 0000<br>+1 (0) 555 123 4567</p>
  </div>
</div>
<div class="abs csocial">
  <span class="dot" style="background:#1da1f2"></span>
  <span class="dot" style="background:#3b5998"></span>
  <span class="dot" style="background:#dd4b39"></span>
  <span class="dot" style="background:#cb2027"></span>
  <span class="dot" style="background:#f26522"></span>
</div>

<footer class="abs footer">PRIVACY POLICY · LEGAL NOTICES · TERMS AND CONDITIONS</footer>

</body>
</html>
```